Redhollow Balloon Festival web site design

"Redhollow" Annual Hot Air Balloon Festival. Be sure to spell Balloon proprely! The largest in the state of Texas. In a park setting with sky divers, live concerts, 5K run event, kids fun zones, food vendors, merchandise, fireowrks, arts & crafts, family oriented, very colorful. Would like to establish themselves as the only event of it's kind in the region. Would like to convey that the event is very cost friendly and a unique experience relative to the other family entertainment opportunities in the area. Easy to read! Would like to emulate various features of www.updraftjubilee.com

Target Market(s)

Families. Kids up to 12. Then adults 25 to 80.

Industry/Entity Type

Entertainment

Requirements
Must have
• Ease of use for participants. There will be an area dedicated to each of the following categories: Attendees, Pilots, Vendors, Volunteers, Performers. Directions, event schedule and tickets will be critical call outs. Then details and sign up info for the other 4 categories. Will need a register/login feature.
Nice to have
• Weather conditions feature, countdown to event clock, social media integration to home page, video channel channel with videos of launch, custom static background image to frame header and content area.
Should not have
• Dark dreary colors or hard to read fonts.

```html
<!DOCTYPE html>
<html lang="en">
<head>
<meta charset="utf-8">
<title>Redhollow Balloon Festival</title>
<link href="https://fonts.googleapis.com/css2?family=Ubuntu:wght@300;400;500&family=Noto+Sans:wght@400;700&display=swap" rel="stylesheet">
<style>
:root{
  --paper:#f6f3ec;
  --blue:#1d63b0;
  --blue-dark:#0f4f9a;
  --blue-text:#1a5ea8;
  --green:#6cbf4a;
  --ink:#1a1a1a;
  --line:#c9cfd6;
  --footer-a:#2f7fe0;
  --footer-b:#1258bf;
}
*{box-sizing:border-box;margin:0;padding:0}
html,body{width:1200px;height:1039px;overflow:hidden}
body{background:linear-gradient(#eceded,#ffffff 60%);font-family:"Noto Sans",sans-serif;color:var(--ink);position:relative}
.page{position:absolute;left:195px;top:0;width:812px;height:1011px;background:var(--paper);box-shadow:0 0 6px rgba(0,0,0,.25)}
.abs{position:absolute}
.logo{left:205px;top:18px;font-family:"Ubuntu",sans-serif;color:var(--blue-text)}
.logo .brand{display:flex;align-items:center;gap:6px;font-size:30px;font-weight:400;line-height:1}
.logo .brand i{width:12px;height:12px;background:var(--green);display:inline-block}
.logo .sub{font-size:10px;letter-spacing:4px;margin-top:3px}
.logo .event{font-size:14px;color:var(--ink);margin-top:2px}
.hero-side{left:1px;top:0;width:195px;height:327px;background:linear-gradient(160deg,#2f9a3a,#e7e21f 55%,#e0b01a)}
.find{left:683px;top:28px;font-size:11px;font-weight:700}
.social{top:25px;width:21px;height:21px;background:var(--blue)}
.search{left:612px;top:61px;width:198px;height:23px;border:1px solid #9aa;background:#fff;font-size:11px;color:#555;padding:4px 6px}
.search svg{position:absolute;right:4px;top:3px}
.hero{left:196px;top:91px;width:614px;height:236px;border:2px solid #fff;background:linear-gradient(90deg,#6aa9e6 0%,#cfe3f7 45%,#a9cdf0 70%,#f0d020 100%)}
.nav{left:0;top:329px;width:812px;height:36px;border-bottom:2px solid var(--blue);display:flex;font-family:"Ubuntu",sans-serif;font-size:14px;color:var(--blue-text)}
.nav span{display:flex;align-items:center;justify-content:center;border-right:1px solid var(--line);padding:0 10px;height:100%}
.nav span:last-child{border:none;flex:1}
.info-h{font-family:"Ubuntu",sans-serif;color:var(--blue-text);font-weight:400}
.vline{width:1px;background:linear-gradient(transparent,#aab4c0,transparent)}
.count{left:10px;top:398px;width:244px;height:38px;border:2px solid var(--blue);font-family:"Ubuntu",sans-serif}
.count .lbl{background:var(--blue);color:#fff;font-size:11px;display:flex;height:15px;align-items:center}
.count .val{display:flex;color:var(--blue-text);font-size:16px;height:19px;align-items:center}
.count span{flex:1;text-align:center}
.tile{top:462px;width:194px;height:83px}
.tile h3{background:var(--blue);color:#fff;font-family:"Ubuntu",sans-serif;font-weight:400;font-size:14px;text-align:right;padding:1px 8px;height:18px;line-height:17px}
.tile div{height:65px}
.welcome{left:13px;top:571px;width:472px}
.welcome h1{font-family:"Ubuntu",sans-serif;font-weight:300;font-size:20px;color:var(--blue-text);margin-bottom:4px}
.welcome p{font-size:10.2px;line-height:15.2px;letter-spacing:.38px;margin-bottom:15.2px}
.gallery-h{left:13px;top:860px;font-family:"Ubuntu",sans-serif;font-weight:300;font-size:15px;color:var(--blue-text)}
.gallery{left:13px;top:886px;width:463px;height:96px;border:1px solid var(--blue-dark)}
.gallery .ph{position:absolute;top:10px;width:112px;height:74px}
.arrow{position:absolute;top:30px;width:19px;height:34px;background:var(--blue)}
.side{left:553px;top:563px;width:240px;height:419px;background:var(--blue);color:#fff;border:2px solid #fff}
.tab{position:absolute;left:0;height:20px;width:146px;background:#fff;color:var(--blue-dark);font-size:10.5px;font-weight:700;padding:3px 5px;clip-path:polygon(0 0,92% 0,100% 50%,92% 100%,0 100%)}
.side .small{position:absolute;font-size:9.5px;line-height:14px}
.side a{color:#fff}
.footer{left:184px;top:1011px;width:833px;height:28px;background:linear-gradient(var(--footer-a),var(--footer-b));color:#fff;font-size:9.5px;text-align:center;line-height:28px;letter-spacing:.4px}
</style>
</head>
<body>
<div class="page">
  <div class="abs hero-side" role="img" aria-label="Large green and yellow hot air balloon rising over trees"></div>
  <div class="abs logo">
    <div class="brand"><i></i>SkyMark</div>
    <div class="sub">CREDIT UNION</div>
    <div class="event">Redhollow Balloon Festival</div>
  </div>
  <div class="abs find">Find us on:</div>
  <div class="abs social" style="left:762px"></div>
  <div class="abs social" style="left:786px;background:#4fb3e8"></div>
  <div class="abs search">Search...
    <svg width="16" height="16" viewBox="0 0 16 16"><circle cx="6.5" cy="6.5" r="4.5" fill="#bfe0ff" stroke="#1d4f8a" stroke-width="1.6"/><line x1="10" y1="10" x2="14.5" y2="14.5" stroke="#1d4f8a" stroke-width="2.4"/></svg>
  </div>
  <div class="abs hero" role="img" aria-label="Colourful hot air balloons rising into a blue sky with white clouds, with a Texas-flag balloon on the right"></div>

  <nav class="abs nav">
    <span>Event Info</span><span>Guest Guide</span><span>Gas Balloons</span><span>Pilots &amp; Crew</span><span>Ballooning</span><span>Operations</span><span>Sponsors</span><span>Merchandise</span><span>Media</span>
  </nav>

  <div class="abs info-h" style="left:12px;top:375px;font-size:15px">Countdown to lift off</div>
  <div class="abs count">
    <div class="lbl"><span>Days</span><span>Hours</span><span>Minutes</span><span>Seconds</span></div>
    <div class="val"><span>228</span>|<span>03</span>|<span>55</span>|<span>10</span></div>
  </div>
  <div class="abs vline" style="left:271px;top:372px;height:80px"></div>
  <div class="abs info-h" style="left:287px;top:377px;font-size:15px">2011 Festival is:</div>
  <div class="abs info-h" style="left:280px;top:403px;font-size:21px">September 16, 17, &amp; 18</div>
  <div class="abs vline" style="left:516px;top:372px;height:80px"></div>
  <div class="abs info-h" style="left:543px;top:377px;font-size:15px">Location of the Event:</div>
  <div class="abs info-h" style="left:540px;top:400px;font-size:15.5px;line-height:19px;width:270px">Willow Bend Park 4120 W. Meadow Lake Parkway Redhollow, Texas 75990</div>

  <div class="abs tile" style="left:1px"><h3>Guest Guide</h3><div role="img" aria-label="Festival balloons on display" style="background:linear-gradient(90deg,#f2d21e,#c8d9ee 55%,#e66b35)"></div></div>
  <div class="abs tile" style="left:206px"><h3>Merchandise</h3><div role="img" aria-label="Balloon envelope being inflated" style="background:linear-gradient(90deg,#f6c81c,#f5a51a 45%,#2a4ea8)"></div></div>
  <div class="abs tile" style="left:411px"><h3>RV Information</h3><div role="img" aria-label="Balloons inflating on the field near parked vehicles" style="background:linear-gradient(90deg,#d9422c,#f1c93b 50%,#5c8a3a)"></div></div>
  <div class="abs tile" style="left:616px"><h3>Buy a Brick</h3><div role="img" aria-label="Festival crowd at the entrance gate" style="background:linear-gradient(#8a7a6a,#b44a3a 60%,#6d5a4a)"></div></div>

  <div class="abs welcome">
    <h1>Welcome To Our Website:</h1>
    <p>Lorem Ipsum is simply dummy text of the printing and typesetting industry. Lorem Ipsum has been the industry's standard dummy text ever since the 1500s, when an unknown printer took a galley of type and scrambled it to make a type specimen book. It has survived not only five centuries, but also the leap into electronic typesetting, remaining essentially unchanged.</p>
    <p>It was popularised in the 1960s with the release of Typeline sheets containing Lorem Ipsum passages, and more recently with desktop publishing software like Folio PageSetter including versions of Lorem Ipsum.</p>
    <p>Lorem Ipsum is simply dummy text of the printing and typesetting industry. Lorem Ipsum has been the industry's standard dummy text ever since the 1500s, when an unknown printer took a galley of type and scrambled it to make a type specimen book. It has survived not only five centuries, but also the leap into electronic typesetting, remaining essentially unchanged.</p>
  </div>
  <div class="abs vline" style="left:516px;top:565px;height:310px"></div>

  <div class="abs gallery-h">Photo Gallery:</div>
  <div class="abs gallery">
    <div class="arrow" style="left:0;border-radius:0 17px 17px 0"><svg width="19" height="34"><path d="M11 11 L6 17 L11 23" stroke="#fff" stroke-width="2.5" fill="none"/></svg></div>
    <div class="ph" role="img" aria-label="Balloons seen from below" style="left:38px;background:linear-gradient(135deg,#c8203a,#f4c51e 50%,#dfe9f4)"></div>
    <div class="ph" role="img" aria-label="Balloons floating over a field" style="left:173px;background:linear-gradient(#4d8ee0,#a8c9ee 70%,#2f4a2a)"></div>
    <div class="ph" role="img" aria-label="Fireworks at night" style="left:304px;background:radial-gradient(circle at 50% 40%,#f3a07a,#2a0a0a 45%,#050505)"></div>
    <div class="arrow" style="right:0;border-radius:17px 0 0 17px"><svg width="19" height="34"><path d="M8 11 L13 17 L8 23" stroke="#fff" stroke-width="2.5" fill="none"/></svg></div>
  </div>

  <aside class="abs side">
    <div class="tab" style="top:6px">Weather:</div>
    <svg class="abs" style="left:180px;top:22px" width="56" height="44" viewBox="0 0 56 44"><circle cx="16" cy="14" r="9" fill="#f7c21c"/><ellipse cx="34" cy="28" rx="20" ry="11" fill="#f2f4f6"/><circle cx="30" cy="20" r="10" fill="#fafbfc"/></svg>
    <div class="small" style="left:5px;top:34px">Updated 02/15/11 1:01a</div>
    <div class="small" style="left:5px;top:52px;font-weight:700">Temperature:<br>Wind:</div>
    <div class="small" style="left:93px;top:52px;font-weight:700">38.3F<br>0.0 mph From<br>SSW (202 Deg.)</div>
    <div class="small" style="left:5px;top:104px"><a href="#">Click here for more detailed info</a></div>
    <div class="tab" style="top:142px">E-Newsletter:</div>
    <div class="abs" style="left:5px;top:174px;width:228px;height:26px;background:#fff;color:#333;font-size:10px;padding:7px 9px">Search...</div>
    <div class="abs" style="left:9px;top:210px;background:#000;border:1.5px solid #fff;border-radius:9px;font-size:9.5px;font-weight:700;padding:1px 7px">Subscribe</div>
    <div class="tab" style="top:249px">Festival Video:</div>
    <div class="abs" style="left:19px;top:274px;width:204px;height:116px;background:linear-gradient(135deg,#b0243a,#f0c41e 45%,#d8e6f3)" role="img" aria-label="Video still of hot air balloons in the sky"></div>
    <div class="abs" style="left:19px;top:382px;width:204px;height:8px;background:#e9e9e9;border-top:2px solid #c52020"></div>
    <div class="small" style="left:0;top:393px;width:236px;text-align:center;line-height:12px"><a href="#">Click here for our video channel</a></div>
  </aside>
</div>
<div class="abs footer">© 2010-2011 Redhollow Annual Hot Air Balloon Festival, Inc.</div>
</body>
</html>
```